Mrs Tully's Menu Design

Our website is MrsTullys.com.au
Please take inspiration in the look and feel, style and tone from the photos of our takeaway restaurant.

We' have been providing our famous Chinese take away in Hollowbrook for over 30 years. We have seen the neighbourhood grow around us and we have grown along with them.
We have had a recent shopfitting (see photos on http://www.mrstullys.com.au).

Red features prominently in our shop design but understand if you would keep it muted or minimal for readability.

We would like to revamp our plain menu to a fresh new look with a typeface that emphasizes familiarity and simple, delicious food.

Reason: Updated brief with more information Would like more designs

Target Market(s)

Our customers are locals who have enjoyed our famous Chinese takeaway for over 30 years. They are mums buying takeout for their family dinner, staff from the surrounding mall shops after a quick, delicious feed and regulars who come in every week for their fix of freshly prepared, familiar Chinese favourites like san choy bow, crispy salt and pepper squid and stir-fried beef in black bean sauce.

Industry/Entity Type

Shop

Requirements
Must have
• Typeface is very important.
It must be readable and convey a classic Chinese menu that oozes familiarity and sincerity. We serve simple, classic Chinese favorites at a economical price
Should not have
• Should not be childish, cartoony or cliched.

```html
<!DOCTYPE html>
<html lang="en">
<head>
<meta charset="utf-8">
<title>Mrs Tully's Menu</title>
<link href="https://fonts.googleapis.com/css2?family=Open+Sans:wght@400;600&family=Questrial&display=swap" rel="stylesheet">
<style>
  :root {
    --bg: #414141;
    --accent: #c9c73c;
    --text: #ffffff;
    --muted: #d9d9d9;
    --ghost: #4a4a44;
  }
  * { margin: 0; padding: 0; box-sizing: border-box; }
  html, body { width: 1200px; height: 773px; overflow: hidden; background: var(--bg); }
  .menu {
    position: relative; width: 1200px; height: 773px; background: var(--bg);
    font-family: "Open Sans", Arial, sans-serif; color: var(--text);
  }
  .backdrop-art {
    position: absolute; left: 440px; top: 20px; width: 560px; height: 680px;
    border-radius: 48%;
    background: radial-gradient(ellipse at center, var(--ghost) 0%, rgba(74,74,68,0.5) 45%, rgba(65,65,65,0) 72%);
  }
  .emblem-art {
    position: absolute; left: 32px; top: 55px; width: 180px; height: 278px;
    border-radius: 40% 40% 12% 12%;
    background: radial-gradient(ellipse at 50% 40%, #5a5a3a 0%, #4a4a3c 60%, #444440 100%);
  }
  .shop-info {
    position: absolute; left: 0; top: 349px; width: 213px; text-align: right;
    color: var(--accent); font-family: "Questrial", Arial, sans-serif;
  }
  .address { font-size: 12.5px; line-height: 16px; }
  .address .upper { text-transform: uppercase; }
  .phone { font-size: 17px; margin-top: 16px; }
  .web { font-size: 13.5px; margin-top: 19px; }
  .hours { font-size: 17px; line-height: 21px; margin-top: 15px; text-transform: uppercase; }

  .specials { position: absolute; width: 420px; }
  .specials h2 {
    font-family: "Questrial", Arial, sans-serif; font-weight: 400; font-size: 18px;
    color: var(--accent); height: 36px; line-height: 22px;
  }
  .specials ul { list-style: none; font-size: 12.5px; line-height: 16.8px; }
  .specials li { display: flex; align-items: baseline; white-space: nowrap; }
  .specials .note { font-size: 10px; color: var(--muted); }
  .specials .leader { flex: 1; border-bottom: 1px dotted var(--muted); margin: 0 2px; transform: translateY(-3px); }
  .specials .price { text-align: right; }

  .col-a { left: 243px; }
  .col-b { left: 746px; }

  .footer-rule {
    position: absolute; left: 100px; top: 691px; width: 1020px; height: 2px;
    background: linear-gradient(90deg, rgba(201,199,60,0) 0%, var(--accent) 45%, var(--accent) 55%, rgba(201,199,60,0) 100%);
  }
  .footer-note {
    position: absolute; left: 0; top: 698px; width: 1245px; text-align: center;
    font-size: 17px; color: var(--text);
  }
</style>
</head>
<body>
<main class="menu">
  <div class="backdrop-art" role="img" aria-label="Large faint guardian lion line illustration in the background"></div>
  <div class="emblem-art" role="img" aria-label="Guardian lion line illustration with paw on a patterned ball"></div>

  <aside class="shop-info">
    <p class="address"><span class="upper">Shop 214 Parkview Mall</span><br><span class="upper">Hollowbrook</span><br>(On Harlow Street,<br>Opp. Town Hall Lawn)</p>
    <p class="phone">Telephone: 9600 2815</p>
    <p class="web">www.mrstullys.com.au</p>
    <p class="hours">Open: 7 days / week<br>10.00am to 9.00pm</p>
  </aside>

  <section class="specials col-a" style="top:56px">
    <h2>Mrs. Tully's Specials</h2>
    <ul>
      <li>Golden Fried Box</li>
      <li>Regular&nbsp;<span class="note">(1 Spring Roll, 1 Curry Meat Pastry, 2 Dim Sims, 1 Prawn Cutlet)</span><span class="leader"></span><span class="price">$6.50</span></li>
      <li>Large&nbsp;<span class="note">(1 Spring Roll, 1 Curry Meat Pastry, 4 Dim Sims, 2 Prawn Cutlets)</span><span class="leader"></span><span class="price">$9.50</span></li>
      <li>Seafood Combination with Oyster Sauce</li>
      <li><span class="note">(King Prawn, Scallop, Calamari, Mushrooms &amp; Babycorn)</span><span class="leader"></span><span class="price">$12.00</span></li>
      <li>Sate Combination&nbsp;<span class="note">(Beef, Chicken &amp; King Prawn)</span><span class="leader"></span><span class="price">$11.00</span></li>
      <li>Garlic &amp; Chilli Combination&nbsp;<span class="note">(Beef, Chicken &amp; King Prawn)</span><span class="leader"></span><span class="price">$11.00</span></li>
      <li>Combination in Oyster Sauce&nbsp;<span class="note">(Beef, Chicken &amp; King Prawn)</span><span class="leader"></span><span class="price">$11.00</span></li>
      <li>Mongolian Lamb Fillet<span class="leader"></span><span class="price">$10.80</span></li>
      <li>Deep Fried Lamb Fillet with Special Sauce<span class="leader"></span><span class="price">$10.80</span></li>
      <li>Braised Chicken with Szechuan Sauce (Hot)<span class="leader"></span><span class="price">$9.90</span></li>
      <li>Braised Chicken with Sweet Chilli Sauce<span class="leader"></span><span class="price">$9.90</span></li>
      <li>Salt &amp; Pepper Squid<span class="leader"></span><span class="price">$10.00</span></li>
      <li>Singapore Fried Noodles<span class="leader"></span><span class="price">$8.50</span></li>
    </ul>
  </section>

  <section class="specials col-a" style="top:386px">
    <h2>Mrs. Tully's Specials</h2>
    <ul>
      <li>Golden Fried Box</li>
      <li>Regular&nbsp;<span class="note">(1 Spring Roll, 1 Curry Meat Pastry, 2 Dim Sims, 1 Prawn Cutlet)</span><span class="leader"></span><span class="price">$6.50</span></li>
      <li>Large&nbsp;<span class="note">(1 Spring Roll, 1 Curry Meat Pastry, 4 Dim Sims, 2 Prawn Cutlets)</span><span class="leader"></span><span class="price">$9.50</span></li>
      <li>Seafood Combination with Oyster Sauce</li>
      <li><span class="note">(King Prawn, Scallop, Calamari, Mushrooms &amp; Babycorn)</span><span class="leader"></span><span class="price">$12.00</span></li>
      <li>Sate Combination&nbsp;<span class="note">(Beef, Chicken &amp; King Prawn)</span><span class="leader"></span><span class="price">$11.00</span></li>
      <li>Garlic &amp; Chilli Combination&nbsp;<span class="note">(Beef, Chicken &amp; King Prawn)</span><span class="leader"></span><span class="price">$11.00</span></li>
      <li>Combination in Oyster Sauce&nbsp;<span class="note">(Beef, Chicken &amp; King Prawn)</span><span class="leader"></span><span class="price">$11.00</span></li>
      <li>Mongolian Lamb Fillet<span class="leader"></span><span class="price">$10.80</span></li>
      <li>Deep Fried Lamb Fillet with Special Sauce<span class="leader"></span><span class="price">$10.80</span></li>
      <li>Braised Chicken with Szechuan Sauce (Hot)<span class="leader"></span><span class="price">$9.90</span></li>
      <li>Braised Chicken with Sweet Chilli Sauce<span class="leader"></span><span class="price">$9.90</span></li>
      <li>Salt &amp; Pepper Squid<span class="leader"></span><span class="price">$10.00</span></li>
      <li>Singapore Fried Noodles<span class="leader"></span><span class="price">$8.50</span></li>
    </ul>
  </section>

  <section class="specials col-b" style="top:57px">
    <h2>Mrs. Tully's Specials</h2>
    <ul>
      <li>Golden Fried Box</li>
      <li>Regular&nbsp;<span class="note">(1 Spring Roll, 1 Curry Meat Pastry, 2 Dim Sims, 1 Prawn Cutlet)</span><span class="leader"></span><span class="price">$6.50</span></li>
      <li>Large&nbsp;<span class="note">(1 Spring Roll, 1 Curry Meat Pastry, 4 Dim Sims, 2 Prawn Cutlets)</span><span class="leader"></span><span class="price">$9.50</span></li>
      <li>Seafood Combination with Oyster Sauce</li>
      <li><span class="note">(King Prawn, Scallop, Calamari, Mushrooms &amp; Babycorn)</span><span class="leader"></span><span class="price">$12.00</span></li>
      <li>Sate Combination&nbsp;<span class="note">(Beef, Chicken &amp; King Prawn)</span><span class="leader"></span><span class="price">$11.00</span></li>
    </ul>
  </section>

  <section class="specials col-b" style="top:221px">
    <h2>Mrs. Tully's Specials</h2>
    <ul>
      <li>Golden Fried Box</li>
      <li>Regular&nbsp;<span class="note">(1 Spring Roll, 1 Curry Meat Pastry, 2 Dim Sims, 1 Prawn Cutlet)</span><span class="leader"></span><span class="price">$6.50</span></li>
      <li>Large&nbsp;<span class="note">(1 Spring Roll, 1 Curry Meat Pastry, 4 Dim Sims, 2 Prawn Cutlets)</span><span class="leader"></span><span class="price">$9.50</span></li>
      <li>Seafood Combination with Oyster Sauce</li>
      <li><span class="note">(King Prawn, Scallop, Calamari, Mushrooms &amp; Babycorn)</span><span class="leader"></span><span class="price">$12.00</span></li>
      <li>Sate Combination&nbsp;<span class="note">(Beef, Chicken &amp; King Prawn)</span><span class="leader"></span><span class="price">$11.00</span></li>
      <li>Garlic &amp; Chilli Combination&nbsp;<span class="note">(Beef, Chicken &amp; King Prawn)</span><span class="leader"></span><span class="price">$11.00</span></li>
      <li>Combination in Oyster Sauce&nbsp;<span class="note">(Beef, Chicken &amp; King Prawn)</span><span class="leader"></span><span class="price">$11.00</span></li>
      <li>Mongolian Lamb Fillet<span class="leader"></span><span class="price">$10.80</span></li>
      <li>Deep Fried Lamb Fillet with Special Sauce<span class="leader"></span><span class="price">$10.80</span></li>
      <li>Braised Chicken with Szechuan Sauce (Hot)<span class="leader"></span><span class="price">$9.90</span></li>
      <li>Braised Chicken with Sweet Chilli Sauce<span class="leader"></span><span class="price">$9.90</span></li>
      <li>Salt &amp; Pepper Squid<span class="leader"></span><span class="price">$10.00</span></li>
      <li>Singapore Fried Noodles<span class="leader"></span><span class="price">$8.50</span></li>
    </ul>
  </section>

  <section class="specials col-b" style="top:523px">
    <h2>Mrs. Tully's Specials</h2>
    <ul>
      <li>Golden Fried Box</li>
      <li>Regular&nbsp;<span class="note">(1 Spring Roll, 1 Curry Meat Pastry, 2 Dim Sims, 1 Prawn Cutlet)</span><span class="leader"></span><span class="price">$6.50</span></li>
      <li>Large&nbsp;<span class="note">(1 Spring Roll, 1 Curry Meat Pastry, 4 Dim Sims, 2 Prawn Cutlets)</span><span class="leader"></span><span class="price">$9.50</span></li>
      <li>Seafood Combination with Oyster Sauce</li>
      <li><span class="note">(King Prawn, Scallop, Calamari, Mushrooms &amp; Babycorn)</span><span class="leader"></span><span class="price">$12.00</span></li>
      <li>Sate Combination&nbsp;<span class="note">(Beef, Chicken &amp; King Prawn)</span><span class="leader"></span><span class="price">$11.00</span></li>
    </ul>
  </section>

  <div class="footer-rule"></div>
  <p class="footer-note">All dishes served with: Fried Rice Boiled Rice Soft Noodles or Thick Rice Noodles $1.50 extra</p>
</main>
</body>
</html>
```